Ironbark lane plumbing plumbing company business card design

Something sinilar to business card i upload it is my old business card design
And have a good watermark with the logo or majority of the logot in rhe background as watermark

Plumbing business similar to uploaded design with a nice watermark of the logo

Font styles to use
Script

Colors

Designer to choose colors to be used in the design.

```html
<!DOCTYPE html>
<html lang="en">
<head>
<meta charset="UTF-8">
<title>Ironbark Lane Plumbing – Business Card</title>
<link rel="stylesheet" href="https://fonts.googleapis.com/css2?family=Montserrat:wght@400;500;600;700;800&display=swap">
<style>
  :root {
    --page-bg: #e6e7e9;
    --card-white: #ffffff;
    --card-black: #141414;
    --ink: #161616;
    --ink-soft: #3a3a3a;
    --brand-blue: #1d7cc7;
    --watermark: #e3e6ea;
    --emboss: #2e2e2e;
  }
  * { box-sizing: border-box; margin: 0; padding: 0; }
  html, body {
    width: 1200px; height: 900px; overflow: hidden;
    background: var(--page-bg);
    font-family: "Montserrat", sans-serif;
  }
  .canvas { position: relative; width: 1200px; height: 900px; }
  .card {
    position: absolute; left: 250px; width: 700px; height: 400px;
    overflow: hidden;
    box-shadow: 0 10px 28px rgba(0,0,0,0.18);
  }
  .card--back { top: 30px; background: var(--card-black); }
  .card--front { top: 470px; background: var(--card-white); }

  /* Back */
  .back-wordmark {
    position: absolute; inset: 0;
    display: flex; align-items: center; justify-content: center;
    padding: 0 40px;
    text-align: center; white-space: nowrap;
    color: var(--emboss);
    font-weight: 800; font-size: 38px; letter-spacing: 2px;
    text-transform: uppercase;
  }

  /* Front */
  .front-wordmark {
    position: absolute; left: 56px; top: 62px;
    display: flex; align-items: center; gap: 14px;
    color: var(--ink);
    font-weight: 800; font-size: 28px; line-height: 1.05;
    text-transform: uppercase; letter-spacing: 1px;
  }
  .front-wordmark__dot {
    width: 18px; height: 18px; border-radius: 50%;
    background: var(--brand-blue); flex: none;
  }
  .watermark {
    position: absolute; right: 40px; top: 110px;
    color: var(--watermark);
    font-weight: 800; font-size: 44px; line-height: 1.05;
    text-align: right; text-transform: uppercase;
  }
  .person { position: absolute; left: 56px; top: 180px; }
  .person__name {
    color: var(--brand-blue);
    font-weight: 600; font-size: 22px; letter-spacing: 0.5px;
    text-transform: uppercase;
  }
  .person__role {
    margin-top: 4px; color: var(--ink-soft);
    font-weight: 400; font-size: 15px;
  }
  .contacts { position: absolute; left: 56px; top: 258px; list-style: none; }
  .contacts__item {
    display: flex; align-items: center; gap: 12px;
    color: var(--ink-soft); font-size: 16px; font-weight: 400;
    height: 28px;
  }
  .contacts__icon { width: 15px; height: 15px; flex: none; }
  .accent-bar {
    position: absolute; left: 0; top: 262px;
    width: 7px; height: 84px; background: var(--brand-blue);
  }
</style>
</head>
<body>
<main class="canvas">

  <section class="card card--back" aria-label="Card back">
    <div class="back-wordmark">Ironbark Lane Plumbing</div>
  </section>

  <section class="card card--front" aria-label="Card front">
    <div class="watermark" aria-hidden="true">Ironbark<br>Lane<br>Plumbing</div>

    <div class="front-wordmark">
      <span class="front-wordmark__dot"></span>
      <span>Ironbark Lane<br>Plumbing</span>
    </div>

    <div class="person">
      <p class="person__name">Dean R. Callow</p>
      <p class="person__role">Director</p>
    </div>

    <span class="accent-bar"></span>

    <ul class="contacts">
      <li class="contacts__item">
        <svg class="contacts__icon" viewBox="0 0 24 24" aria-hidden="true">
          <path fill="#1d7cc7" d="M6.6 10.8a15.1 15.1 0 0 0 6.6 6.6l2.2-2.2a1 1 0 0 1 1-.25 11.4 11.4 0 0 0 3.6.57 1 1 0 0 1 1 1V20a1 1 0 0 1-1 1A17 17 0 0 1 3 4a1 1 0 0 1 1-1h3.5a1 1 0 0 1 1 1c0 1.250.2 2.450.57 3.57a1 1 0 0 1-.25 1z"/>
        </svg>
        <span>0412 555 019</span>
      </li>
      <li class="contacts__item">
        <svg class="contacts__icon" viewBox="0 0 24 24" aria-hidden="true">
          <rect x="2.5" y="5" width="19" height="14" rx="1.5" fill="none" stroke="#1d7cc7" stroke-width="2"/>
          <path d="M3 6l9 7 9-7" fill="none" stroke="#1d7cc7" stroke-width="2"/>
        </svg>
        <span>info@ironbarklaneplumbing.com</span>
      </li>
      <li class="contacts__item">
        <svg class="contacts__icon" viewBox="0 0 24 24" aria-hidden="true">
          <circle cx="12" cy="12" r="9.5" fill="none" stroke="#1d7cc7" stroke-width="2"/>
          <path d="M2.5 12h19M12 2.5c3 3 3 16 0 19M12 2.5c-3 3-3 16 0 19" fill="none" stroke="#1d7cc7" stroke-width="1.6"/>
        </svg>
        <span>www.ironbarklaneplumbing.com</span>
      </li>
    </ul>
  </section>

</main>
</body>
</html>
```